Letter head to include new logo and the following services:<br/><br/>Static Security, Mobile Patrols, Alarm Response & Key Holding, Alarm & CCTV Monitoring, Welfare Hire.<br/><br/>Phone: 0800 417 3926<br/>E-mail: security@tqv-holdings.co.uk<br/><br/>Southern Office:<br/>TQV Security & Monitoring<br/>2nd Floor<br/>7 Larchmere Close<br/>London<br/>N15 4PW<br/><br/>Northern Office:<br/>TQV Security & Monitoring<br/>Gateway 14 Vehicle Compound<br/>Pelham Street<br/>Aston<br/>Sheffield<br/>S21 7HT<br/><br/>I need the files as PDF and an editable Microsoft Word Document. See attached file from my other business as an example. Do not copy information from uploaded word document, its just an example only. Logo also attached.<br/><br/><br/>SEE OTHER PROJECTS, THEY ARE ALL LINKED<br/> <br/>

```html
<!DOCTYPE html>
<html lang="en">
<head>
<meta charset="utf-8">
<title>TQV Security &amp; Monitoring – Letterhead</title>
<link href="https://fonts.googleapis.com/css2?family=Source+Sans+3:wght@400;600;700&family=Arimo:wght@700&display=swap" rel="stylesheet">
<style>
  :root {
    --brand-blue: #1668bd;
    --ink: #3a3a3a;
    --ink-soft: #4a4a4a;
    --icon-dark: #2b2b2b;
    --rule: #9a9a9a;
    --paper: #fbfbfb;
    --backdrop: #e6e6e6;
  }
  * { margin: 0; padding: 0; box-sizing: border-box; }
  html, body { width: 1200px; height: 1200px; overflow: hidden; background: var(--backdrop); }
  .letterhead {
    position: absolute; left: 188px; top: 20px;
    width: 824px; height: 1160px;
    background: var(--paper);
    font-family: "Source Sans 3", Arial, sans-serif;
    color: var(--ink);
    overflow: hidden;
  }
  .brand {
    position: absolute; left: 63px; top: 76px;
    display: flex; align-items: center; gap: 10px;
  }
  .brand-dot { width: 22px; height: 22px; border-radius: 50%; background: var(--brand-blue); }
  .brand-name { font-size: 22px; font-weight: 700; color: var(--brand-blue); }
  .services {
    position: absolute; left: 552px; top: 38px;
    border-left: 1px solid var(--rule);
    padding-left: 12px;
    list-style: none;
  }
  .services li {
    display: flex; align-items: center; gap: 7px;
    font-size: 14px; line-height: 19px; color: var(--icon-dark);
  }
  .services svg { width: 13px; height: 13px; flex: none; }
  .salutation {
    position: absolute; left: 62px; top: 248px;
    font-family: "Arimo", Arial, sans-serif; font-weight: 700;
    font-size: 18px; color: var(--ink-soft);
  }
  .letter-body {
    position: absolute; left: 62px; top: 293px; width: 699px;
    font-size: 17.2px; line-height: 21.6px; color: var(--ink-soft);
    text-align: justify;
  }
  .letter-body p + p { margin-top: 21.6px; }
  .signature {
    position: absolute; left: 64px; top: 877px; width: 153px; height: 73px;
    background: linear-gradient(90deg, #e9e9e9, #f4f4f4);
    border-radius: 4px;
  }
  .footer-bar { position: absolute; left: 60px; top: 1079px; width: 13px; height: 81px; background: var(--brand-blue); }
  .contact {
    position: absolute; left: 84px; top: 1075px;
    font-size: 13px; line-height: 19.5px; color: #222;
  }
  .contact .icon { display: inline-block; vertical-align: -1px; width: 11px; height: 10px; margin-right: 3px; }
  .contact .gap { margin-left: 7px; }
  .office-label { color: var(--brand-blue); font-weight: 700; margin-right: 7px; }
  .footer-rule { position: absolute; left: 73px; top: 1141px; width: 530px; height: 1px; background: #555; }
  .web-tag { position: absolute; left: 598px; top: 1131px; width: 176px; height: 21px; }
  .web-tag span {
    position: absolute; inset: 0; display: flex; align-items: center; justify-content: center;
    color: #fff; font-size: 13px; letter-spacing: 1px;
  }
</style>
</head>
<body>
<main class="letterhead">
  <header>
    <div class="brand">
      <span class="brand-dot"></span>
      <span class="brand-name">TQV Security &amp; Monitoring</span>
    </div>
    <ul class="services">
      <li><svg viewBox="0 0 14 14"><circle cx="7" cy="7" r="7" fill="var(--icon-dark)"/><rect x="4.5" y="6.5" width="5" height="4" fill="#fff"/><path d="M5.3 6.5V5a1.7 1.7 0 0 1 3.4 0v1.5" stroke="#fff" stroke-width="1.1" fill="none"/></svg>Static Security,</li>
      <li><svg viewBox="0 0 14 14"><circle cx="7" cy="7" r="7" fill="var(--icon-dark)"/><rect x="4.5" y="6.5" width="5" height="4" fill="#fff"/><path d="M5.3 6.5V5a1.7 1.7 0 0 1 3.4 0v1.5" stroke="#fff" stroke-width="1.1" fill="none"/></svg>Mobile Patrols,</li>
      <li><svg viewBox="0 0 14 14"><circle cx="7" cy="7" r="7" fill="var(--icon-dark)"/><rect x="4.5" y="6.5" width="5" height="4" fill="#fff"/><path d="M5.3 6.5V5a1.7 1.7 0 0 1 3.4 0v1.5" stroke="#fff" stroke-width="1.1" fill="none"/></svg>Alarm Response &amp; Key Holding,</li>
      <li><svg viewBox="0 0 14 14"><circle cx="7" cy="7" r="7" fill="var(--icon-dark)"/><rect x="4.5" y="6.5" width="5" height="4" fill="#fff"/><path d="M5.3 6.5V5a1.7 1.7 0 0 1 3.4 0v1.5" stroke="#fff" stroke-width="1.1" fill="none"/></svg>Alarm &amp; CCTV Monitoring,</li>
      <li><svg viewBox="0 0 14 14"><circle cx="7" cy="7" r="7" fill="var(--icon-dark)"/><rect x="4.5" y="6.5" width="5" height="4" fill="#fff"/><path d="M5.3 6.5V5a1.7 1.7 0 0 1 3.4 0v1.5" stroke="#fff" stroke-width="1.1" fill="none"/></svg>Welfare Hire.</li>
    </ul>
  </header>

  <p class="salutation">Dear Mr. Ellison,</p>

  <section class="letter-body">
    <p>Lorem Ipsum is simply dummy text of the printing and typesetting industry. Lorem Ipsum has been the industry's standard dummy text ever since the 1500s, when an unknown printer took a galley of type and scrambled it to make a type specimen book. It has survived not only five centuries, but also the leap into electronic typesetting, remaining essentially unchanged.</p>
    <p>The standard chunk of Lorem Ipsum used since the 1500s is reproduced below for those interested. Sections 1.10.32 and 1.10.33 from "de Finibus Bonorum et Malorum" by Aurelio Maspen are also reproduced in their exact original form, accompanied by English versions from the 1914 translation by H. Pembury</p>
    <p>Lorem Ipsum is simply dummy text of the printing and typesetting industry. Lorem Ipsum has been the industry's standard dummy text ever since the 1500s, when an unknown printer took a galley of type and scrambled it to make a type specimen book. It has survived not only five centuries, but also the leap into electronic typesetting, remaining essentially unchanged. It was popularised in the</p>
    <p>Lorem Ipsum is simply dummy text of the printing and typesetting industry. Lorem Ipsum has been the industry's standard dummy text ever since the 1500s, when an unknown printer took a galley of type and scrambled it to make a type specimen book. It has survived not only five centuries, but also the leap into electronic typesetting, remaining essentially unchanged. It was popularised in the</p>
    <p>Lorem Ipsum is simply dummy text of the printing and typesetting industry. Lorem Ipsum has been the industry's standard dummy text ever since the 1500s, when an unknown printer took a galley of type and scrambled it to make a type specimen book.</p>
  </section>

  <div class="signature" role="img" aria-label="Handwritten signature of the sender"></div>

  <footer>
    <div class="footer-bar"></div>
    <div class="contact">
      <div>
        <svg class="icon" viewBox="0 0 12 10"><path d="M1 3.5C1 2 3 1 6 1s5 1 5 2.5l-2 .8-.8-1.3H3.8L3 4.3z M3 5h6l1.5 4h-9z" fill="var(--brand-blue)"/></svg>0800 417 3926
        <svg class="icon gap" viewBox="0 0 12 10"><rect x="0.5" y="1" width="11" height="8" fill="var(--brand-blue)"/><path d="M0.5 1.5L6 6l5.5-4.5" stroke="#fff" stroke-width="1" fill="none"/></svg>security@tqv-holdings.co.uk
      </div>
      <div><span class="office-label">Northern Office:-</span>Gateway 14, Vehicle Compound, Pelham Street, Aston, Sheffield, S21 7HT</div>
      <div><span class="office-label">Southern Office:-</span> 2nd Floor, 7 Larchmere Close, London, N15 4PW</div>
    </div>
    <div class="footer-rule"></div>
    <div class="web-tag">
      <svg viewBox="0 0 176 21" width="176" height="21"><path d="M8 0H168L176 10.5L168 21H8L0 10.5Z" fill="var(--brand-blue)"/></svg>
      <span>www.tqv-holdings.co.uk</span>
    </div>
  </footer>
</main>
</body>
</html>
```